Brenwick Realty
Business cards and stationery
Brenwick Realty - Real Estate
Creative Brief
Modern
Marian Talcott
Director
Level 4 218 Garnet Lane Melbourne VIC 3000
marian@brenwickrealty-example.com.au
www.brenwickrealty-example.com.au
Brenwick Summit Realty 518902K Licensee Marian Talcott
Stationery needs to have the licensee info on the bottom of letterhead
black background logo in centre

```html
<!DOCTYPE html>
<html lang="en">
<head>
<meta charset="utf-8">
<title>Brenwick Realty – Business Card</title>
<link href="https://fonts.googleapis.com/css2?family=Montserrat:wght@400;600;700&display=swap" rel="stylesheet">
<style>
  :root {
    --backdrop: #3b3c3e;
    --blue: #2a8fd8;
    --blue-deep: #176db6;
    --magenta: #d0187a;
    --magenta-deep: #a5105e;
    --ink: #0d0d0f;
    --white: #ffffff;
    --muted: #c9c9cf;
  }
  * { margin: 0; padding: 0; box-sizing: border-box; }
  html, body { width: 1200px; height: 646px; overflow: hidden; }
  body {
    background: var(--backdrop);
    font-family: "Montserrat", Arial, sans-serif;
    position: relative;
  }
  .card {
    position: absolute;
    top: 165px;
    width: 520px;
    height: 316px;
    border-radius: 4px;
    overflow: hidden;
    box-shadow: 0 10px 30px rgba(0,0,0,.35);
  }
  /* Back face */
  .card-back {
    left: 50px;
    background: linear-gradient(135deg, var(--blue) 0%, var(--blue-deep) 100%);
    color: var(--white);
  }
  .card-back .brand {
    position: absolute; top: 118px; left: 0; right: 0;
    text-align: center; font-size: 34px; font-weight: 700; letter-spacing: .5px;
  }
  .card-back .website {
    position: absolute; top: 170px; left: 0; right: 0;
    text-align: center; font-size: 11px; letter-spacing: 1px;
  }
  .card-back .licence {
    position: absolute; bottom: 18px; left: 22px;
    font-size: 8.5px; letter-spacing: .4px; opacity: .9;
  }
  .card-back .tagline {
    position: absolute; top: 18px; right: 22px;
    font-size: 8.5px; letter-spacing: .4px; opacity: .9;
  }
  /* Front face */
  .card-front {
    left: 630px;
    background: var(--ink);
    color: var(--white);
  }
  .card-front .swoosh { position: absolute; top: 0; left: 0; }
  .card-front .person {
    position: absolute; top: 20px; right: 34px; text-align: left;
  }
  .person .name { font-size: 15px; font-weight: 600; }
  .person .role { font-size: 9px; color: #f3d3e4; margin-top: 3px; }
  .card-front .brand {
    position: absolute; left: 34px; top: 186px;
    font-size: 28px; font-weight: 700; color: var(--magenta);
  }
  .card-front .details {
    position: absolute; left: 300px; top: 128px;
    font-size: 9px; line-height: 1.55; color: var(--muted);
  }
  .details .address { margin-bottom: 10px; }
  .details .line { display: flex; align-items: center; gap: 7px; height: 17px; }
  .details svg { width: 11px; height: 11px; flex: none; }
</style>
</head>
<body>
  <section class="card card-back">
    <p class="tagline">Brenwick Realty - Real Estate</p>
    <h1 class="brand">Brenwick Realty</h1>
    <p class="website">www.brenwickrealty-example.com.au</p>
    <p class="licence">Licensee Brenwick Summit Realty 518902K</p>
  </section>

  <section class="card card-front">
    <svg class="swoosh" width="520" height="130" viewBox="0 0 520 130">
      <defs>
        <linearGradient id="bandGrad" x1="0" x2="1">
          <stop offset="0" stop-color="var(--magenta-deep)"/>
          <stop offset="1" stop-color="var(--magenta)"/>
        </linearGradient>
      </defs>
      <path d="M0 0 H520 V78 C420 72 330 58 250 70 C170 82 80 110 0 118 Z" fill="url(#bandGrad)"/>
      <path d="M0 124 C90 114 170 90 250 78 C330 66 420 80 520 86" fill="none" stroke="var(--blue)" stroke-width="5"/>
    </svg>
    <div class="person">
      <p class="name">Marian Talcott</p>
      <p class="role">Director</p>
    </div>
    <p class="brand">Brenwick Realty</p>
    <div class="details">
      <p class="address">Level 4<br>218 Garnet Lane<br>Melbourne VIC 3000</p>
      <p class="line">
        <svg viewBox="0 0 12 12"><circle cx="6" cy="6" r="6" fill="var(--magenta)"/><path d="M4 3.2l1 1-.6.8c.4.9 1 1.5 1.8 1.8l.8-.6 1 1-.7.9C5.6 8 4 6.4 3.3 4.2z" fill="#fff"/></svg>
        03 9000 4812
      </p>
      <p class="line">
        <svg viewBox="0 0 12 12"><circle cx="6" cy="6" r="6" fill="var(--magenta)"/><rect x="4.2" y="2.8" width="3.6" height="6.4" rx=".6" fill="#fff"/></svg>
        0400 000 317
      </p>
      <p class="line">
        <svg viewBox="0 0 12 12"><circle cx="6" cy="6" r="6" fill="var(--magenta)"/><rect x="3" y="4.5" width="6" height="4" fill="#fff"/><rect x="4" y="2.8" width="4" height="2" fill="#fff"/></svg>
        03 9000 4813
      </p>
      <p class="line">
        <svg viewBox="0 0 12 12"><circle cx="6" cy="6" r="6" fill="var(--magenta)"/><rect x="3" y="4" width="6" height="4.2" fill="#fff"/><path d="M3 4l3 2.4L9 4" fill="none" stroke="var(--magenta)" stroke-width=".7"/></svg>
        marian@brenwickrealty-example.com.au
      </p>
    </div>
  </section>
</body>
</html>
```